Presentation card Venture KELO - Tech Incubator from Perú

We need a Design to promote the incubator of technology Startups.
We are in Perú, we work with a string tech filter and develop enterprenurship competencies in the Startup team.
The card is to facilitators and staff memebers of VentureKELO.
We want a clear, modern, tech and agile Design.

We work to help New enterprises of technology here in Perú, we expect the candidates have a big competencies to Research and develop technological products.

We work using methodologies from QRB, Folmestry, Brakewell and Harrowgate univeesities. Our book base is the disciplina of enterpreneur.

We work events all year using diferent formats: Brightforge, Vorne price, OPRA Model Competition you can use these logros in your Design.

Set the name, role, email, cell phone number, address.

Example:
// Contact info section
Tobías Quiroveda
Swift Modeling Hub Manager
tobias.quiroveda@kelo-example.pe
(511) 999 000 417

// Address info section
VentureKELO
Technology-based business incubator
Av. Los Cedrales 884, Valdora
Lima - Perú
web: venture-kelo-example.org.pe
email: venture@kelo-example.pe
phone number: (511) 3926508 ext. 4418

// (optional)Lema section
Making happy using technology

// Social network section
facebook: venturekelooficial

Target Market(s)

Enterprenurship, CTO, Investors, Companies interested on open innovation services

Industry/Entity Type

Information Technology

Contact Information for Business Card

Name, Role, Email, Cell phone number

Colors

Designer to choose colors to be used in the design.

Requirements
Must have
• Logo forms and colors
Nice to have
• I add pictures of the leaders of incubator
Should not have
• No vertical designs

```html
<!DOCTYPE html>
<html lang="en">
<head>
<meta charset="utf-8">
<title>Venture KELO – Business Card</title>
<link rel="stylesheet" href="https://fonts.googleapis.com/css2?family=Open+Sans:wght@400;600;700;800&display=swap">
<style>
  :root {
    --stage: #222222;
    --card-dark: #2d2c2e;
    --card-light: #f6f6f6;
    --brand: #bd3760;
    --ink: #2b2a2c;
    --white: #ffffff;
  }
  * { margin: 0; padding: 0; box-sizing: border-box; }
  html, body {
    width: 980px; height: 1200px; overflow: hidden;
    background: var(--stage);
    font-family: "Open Sans", sans-serif;
  }
  .card {
    position: absolute; left: 126px; width: 757px; height: 432px;
    overflow: hidden;
  }
  .card--front { top: 102px; background: var(--card-dark); }
  .card--back  { top: 642px; background: var(--card-light); }

  .wordmark {
    position: absolute; left: 20px; top: 26px;
    display: flex; align-items: flex-start; gap: 12px;
  }
  .wordmark__square { width: 16px; height: 16px; background: var(--brand); margin-top: 10px; }
  .wordmark__name {
    font-weight: 800; font-size: 46px; line-height: 0.95; letter-spacing: -0.5px;
    text-transform: uppercase;
  }
  .card--front .wordmark__name { color: var(--white); }
  .card--back .wordmark__name { color: var(--ink); }

  .events { position: absolute; left: 0; right: 0; top: 334px; text-align: center; }
  .events__title { color: var(--brand); font-weight: 700; font-size: 21px; line-height: 28px; letter-spacing: 0.3px; }
  .events__list { color: var(--white); font-size: 20px; line-height: 28px; letter-spacing: 0.5px; }
  .events__rule { position: absolute; top: 366px; height: 2px; background: var(--white); }
  .events__rule--left { left: 0; width: 107px; }
  .events__rule--right { left: 650px; width: 107px; }

  .person__bar { position: absolute; left: 0; top: 249px; width: 13px; height: 50px; background: var(--brand); }
  .person__name {
    position: absolute; left: 27px; top: 236px;
    color: var(--brand); font-weight: 700; font-size: 29px; letter-spacing: 0.2px;
  }
  .person__role { position: absolute; left: 27px; top: 280px; color: var(--ink); font-size: 18px; letter-spacing: 0.3px; }
  .divider { position: absolute; left: 27px; top: 324px; width: 702px; height: 1.5px; background: var(--brand); }

  .contact { position: absolute; left: 27px; top: 343px; list-style: none; }
  .contact__item {
    display: flex; align-items: center; height: 33px;
    color: var(--ink); font-size: 19px; letter-spacing: 1px;
  }
  .contact__icon { width: 14px; height: 14px; margin-right: 12px; fill: var(--brand); }
  .country { position: absolute; right: 28px; top: 343px; height: 33px; line-height: 33px; color: var(--ink); font-size: 19px; letter-spacing: 1px; }
  .footer-band { position: absolute; left: 0; bottom: 0; width: 757px; height: 11px; }
</style>
</head>
<body>
  <section class="card card--front" aria-label="Card front">
    <div class="wordmark"><span class="wordmark__square"></span><span class="wordmark__name">Venture<br>KELO</span></div>
    <span class="events__rule events__rule--left"></span>
    <span class="events__rule events__rule--right"></span>
    <div class="events">
      <p class="events__title">We work events all year using diferent formats:</p>
      <p class="events__list">Brightforge | Vorne price | OPRA Model Competition</p>
    </div>
  </section>

  <section class="card card--back" aria-label="Card back">
    <div class="wordmark"><span class="wordmark__square"></span><span class="wordmark__name">Venture<br>KELO</span></div>
    <span class="person__bar"></span>
    <h1 class="person__name">TOBÍAS QUIROVEDA</h1>
    <p class="person__role">Senior Software Development Engineer</p>
    <span class="divider"></span>
    <ul class="contact">
      <li class="contact__item">
        <svg class="contact__icon" viewBox="0 0 16 16" aria-hidden="true"><path d="M3.6 1.2l2.3 2.6-1.3 1.7c.9 2 2.6 3.7 4.6 4.6l1.7-1.3 2.6 2.3-1.3 2.6C7.1 13.6 2.4 8.9 1 3.2z"/></svg>
        012 345 0417
      </li>
      <li class="contact__item">
        <svg class="contact__icon" viewBox="0 0 16 16" aria-hidden="true"><path d="M1 4h14v1.2L8 9.4 1 5.2z"/><path d="M1 6.6l7 4.2 7-4.2V13H1z"/></svg>
        info@venturekelo-example.com
      </li>
    </ul>
    <p class="country">Perú</p>
    <svg class="footer-band" viewBox="0 0 757 11" preserveAspectRatio="none" aria-hidden="true">
      <polygon points="0,0 612,0 601,11 0,11" fill="var(--ink)"/>
      <polygon points="623,11 634,0 757,0 757,11" fill="var(--brand)"/>
    </svg>
  </section>
</body>
</html>
```